National online rug retailer needs a home page design

See the LoomNest logo and create a home page design around that color theme. Details are spelled out in word document uploaded below.
Updates

Apparently this website did not take my attachement showing the logo and basic requirements.  If you would send me your email address, I will send you the attachment directly.
Best regards,
Ned Carver
ncarver@qwplex.com

Target Market(s)

The target market is home owners 25 to 75 years old with combined incomes over $100,000 per year.

Industry/Entity Type

Online

Requirements
Must have
• Lots of white space with black letters and creative use of red and possibly one other color. Would like a compelling call to action button.

```html
<!DOCTYPE html>
<html lang="en">
<head>
<meta charset="utf-8">
<title>LoomNest.com — Home</title>
<link rel="stylesheet" href="https://fonts.googleapis.com/css2?family=Open+Sans:wght@400;600&family=PT+Sans+Narrow&family=Yanone+Kaffeesatz:wght@300;400&display=swap">
<style>
:root{
  --red:#d0222b;
  --red-dark:#b8141c;
  --ink:#222;
  --grey-text:#555;
  --nav:#333;
  --frame:#bdbdbd;
  --panel:#f0f0f0;
  --line:#d9d9d9;
  --white:#fff;
  --brown:#6b3b12;
}
*{box-sizing:border-box;margin:0;padding:0}
html,body{width:1008px;height:1200px;overflow:hidden;background:var(--white)}
body{font-family:"Open Sans",Arial,sans-serif;color:var(--ink);position:relative}
a{color:inherit;text-decoration:none}
.abs{position:absolute}

/* header */
.brand{left:12px;top:12px;display:flex;align-items:center;gap:8px}
.brand-mark{width:30px;height:30px;background:var(--red)}
.brand-name{font-size:34px;font-weight:400;color:#444;letter-spacing:-.5px;line-height:1}
.tagline{left:86px;top:60px;font-size:10px;color:#666}
.search{left:297px;top:25px;width:367px;height:35px;border:4px solid #aaa;background:#e6e6e6;padding:0 8px;font-size:13px;line-height:27px;color:#333}
.search-btn{left:673px;top:25px;width:34px;height:34px}
.cart{right:30px;top:13px;font-size:11px;color:#111}
.phone{right:7px;top:28px;font-size:17px;color:#222}
.account{right:140px;top:58px;font-size:11px;color:var(--red);font-weight:600}
.chat{right:7px;top:54px;width:94px;height:24px;background:var(--red);color:#fff;border-radius:3px;font-size:10px;font-weight:600;text-align:center;line-height:24px}

/* nav */
.nav{left:0;top:86px;width:1008px;height:42px;background:var(--nav);display:flex;justify-content:space-around;align-items:center;font-family:"Yanone Kaffeesatz",sans-serif;font-weight:300;font-size:20px;color:#fff}

/* sidebar */
.sidebar{left:11px;top:135px;width:172px;height:372px;background:var(--frame);padding:7px}
.sidebar-inner{background:#fff;height:100%;padding:14px 13px;border:1px solid #e5e5e5}
.filter{background:var(--red);color:#fff;font-family:"Yanone Kaffeesatz",sans-serif;font-weight:300;font-size:19px;height:32px;line-height:32px;padding:0 7px;display:flex;justify-content:space-between;border-bottom:1px solid #e55}
.filter.open{background:var(--red-dark)}
.sub{background:#cfcfcf;border-left:5px solid #999;font-size:12px;height:22px;line-height:22px;padding-left:12px;border-bottom:1px solid #eee;color:#222}

/* banner */
.banner{left:200px;top:128px;width:611px;height:276px;background:#2b2b2b;padding:0 4px}
.banner-art{position:absolute;left:4px;top:0;width:602px;height:247px;background:linear-gradient(115deg,#fff 0 32%,#e7b49a 45%,#b9473c 60%,#8a3a24 75%,#c39a6a 100%)}
.sale-tags{position:absolute;left:26px;top:20px;width:170px;height:80px;background:linear-gradient(90deg,#d6262a,#e6a233,#8ab02b,#e0611f);border-radius:6px}
.hurry{position:absolute;left:30px;top:128px;font-family:"Yanone Kaffeesatz",sans-serif;font-weight:300;font-size:38px;color:#333;line-height:1}
.off{position:absolute;left:30px;top:170px;font-family:"Open Sans",sans-serif;font-weight:600;font-size:34px;color:#222;letter-spacing:-1px}
.corner{position:absolute;right:0;top:0;width:170px;height:125px;overflow:hidden}
.dots{position:absolute;right:6px;bottom:8px;display:flex;gap:10px}
.dots i{width:14px;height:14px;border-radius:50%;background:var(--red);display:block}
.dots i:first-child{background:#fff}

/* products */
.showcase{left:200px;top:404px;width:611px;height:456px;background:var(--panel);border-top:3px solid #ccc;padding:0 9px}
.sec-head{display:flex;justify-content:space-between;align-items:flex-end;height:48px;padding:0 3px 6px}
.sec-title{font-family:"Yanone Kaffeesatz",sans-serif;font-weight:300;font-size:30px;color:#333;line-height:1}
.more{font-family:"Yanone Kaffeesatz",sans-serif;font-size:15px;color:#444}
.grid{background:#fff;border:1px solid #ddd;padding:7px 6px;display:flex;justify-content:space-between;height:124px}
.tile{width:189px;height:108px}
.labels{display:flex;justify-content:space-between;padding:6px 8px 0}
.label{width:190px;font-family:"PT Sans Narrow",sans-serif;font-size:13.5px;text-transform:uppercase;color:#111;line-height:1.2}
.label span{display:block;text-transform:none;font-size:12.5px;color:var(--brown)}
.rule{height:1px;background:#ccc;margin:14px 3px 0}

/* right column */
.related{left:827px;top:135px;width:172px;height:697px;background:var(--frame);padding:7px}
.related-inner{background:var(--line);height:100%;padding:16px 13px;border:2px solid #fff}
.related-head{background:#555;color:#fff;font-family:"Yanone Kaffeesatz",sans-serif;font-weight:300;font-size:20px;height:29px;line-height:29px;padding-left:8px;margin-bottom:10px}
.card{background:#fff;height:114px;margin-bottom:10px;padding:6px 8px}
.card-art{width:115px;height:71px}
.card-name{font-family:"PT Sans Narrow",sans-serif;font-size:13px;margin-top:3px;line-height:1.1}
.card-price{font-family:"PT Sans Narrow",sans-serif;font-size:11px;color:var(--red)}

/* footer */
.footer-rule{left:0;top:967px;width:1008px;height:6px;background:#3a3a3a}
.footer-rule2{left:0;top:978px;width:1008px;height:10px;background:#ccc}
.fcol{top:1010px;font-size:11px;color:#555;line-height:13.5px}
.fcol h3{font-family:"Yanone Kaffeesatz",sans-serif;font-weight:400;font-size:20px;color:var(--red);margin-bottom:8px;line-height:1}
.badges{left:692px;top:1018px;width:310px;display:flex;flex-wrap:wrap;align-items:center;gap:10px 6px}
.badge{height:30px;border-radius:3px}
</style>
</head>
<body>

<header>
  <div class="abs brand"><span class="brand-mark"></span><span class="brand-name">LoomNest.com</span></div>
  <div class="abs tagline">woven comfort for every room</div>
  <div class="abs search">SEARCH PRODUCT</div>
  <svg class="abs search-btn" viewBox="0 0 34 34" aria-label="Search">
    <circle cx="17" cy="17" r="16" fill="#333"/>
    <circle cx="15" cy="15" r="6.5" fill="none" stroke="#fff" stroke-width="2.5"/>
    <line x1="19.5" y1="19.5" x2="25" y2="25" stroke="#fff" stroke-width="3.5" stroke-linecap="round"/>
  </svg>
  <div class="abs cart">Items: &nbsp;| Total $0.00 | View Cart | Checkout</div>
  <div class="abs phone">Order toll-free: 1-888-555-0142</div>
  <div class="abs account">My Account | Sign In</div>
  <div class="abs chat">Live Help &nbsp;OFFLINE</div>
</header>

<nav class="abs nav">
  <a>Home</a><a>Selection guides</a><a>Rug Care</a><a>FAQ</a><a>Return Policy</a><a>Free Shipping</a><a>Clearance Rugs</a>
</nav>

<aside class="abs sidebar">
  <div class="sidebar-inner">
    <div class="filter open"><span>RUG THEME</span><span>-</span></div>
    <div class="sub">Traditional</div>
    <div class="sub">Transitional</div>
    <div class="sub">Casual</div>
    <div class="filter"><span>COLOR WAY</span><span>+</span></div>
    <div class="filter"><span>SIZE</span><span>+</span></div>
    <div class="filter"><span>SHAPE</span><span>+</span></div>
    <div class="filter"><span>FIBER CONTENT</span><span>+</span></div>
    <div class="filter"><span>MFGR. BRAND</span><span>+</span></div>
    <div class="filter"><span>MFGR.COLLECTION</span><span>+</span></div>
    <div class="filter"><span>PRICE</span><span>+</span></div>
  </div>
</aside>

<section class="abs banner">
  <div class="banner-art" role="img" aria-label="Stack of patterned area rugs in red, rust and cream tones">
    <div class="sale-tags" role="img" aria-label="Hanging sale tags"></div>
    <div class="hurry">HURRY UP!</div>
    <div class="off">40-50% OFF</div>
    <svg class="corner" viewBox="0 0 170 125">
      <polygon points="0,0 60,0 170,95 170,125" fill="#c8141b"/>
      <text x="105" y="52" fill="#fff" font-family="Yanone Kaffeesatz, sans-serif" font-size="28" font-weight="300" transform="rotate(38 105 52)" text-anchor="middle">check now</text>
    </svg>
  </div>
  <div class="dots"><i></i><i></i><i></i></div>
</section>

<main class="abs showcase">
  <div class="sec-head"><span class="sec-title">top seller</span><span class="more">+ more</span></div>
  <div class="grid">
    <div class="tile" role="img" aria-label="Grey patterned rug in a modern bedroom" style="background:linear-gradient(180deg,#b9bcc0,#6f7378)"></div>
    <div class="tile" role="img" aria-label="Dark rug beside a white bed" style="background:linear-gradient(180deg,#8c8c8c,#2c2c2c)"></div>
    <div class="tile" role="img" aria-label="Red traditional rug under a red armchair" style="background:linear-gradient(180deg,#7a3a2a,#8e1e1e)"></div>
  </div>
  <div class="labels">
    <div class="label">Tidewater Imports<span>+more</span></div>
    <div class="label">Harbor Weave<span>+more</span></div>
    <div class="label">Crimson Sala Co<span>+more</span></div>
  </div>
  <div class="rule"></div>
  <div class="sec-head"><span class="sec-title">new arrivals</span><span class="more">+ more</span></div>
  <div class="grid">
    <div class="tile" role="img" aria-label="Brown rug with cream floral outlines" style="background:linear-gradient(135deg,#5a2e1c,#3a1a10)"></div>
    <div class="tile" role="img" aria-label="Black, white and grey geometric shag rug" style="background:linear-gradient(135deg,#c8a266,#444 45%,#ddd 70%,#b78a50)"></div>
    <div class="tile" role="img" aria-label="Cream rug with green and red tile shapes" style="background:linear-gradient(135deg,#e9e5dc,#8ea04a 55%,#c73a2a)"></div>
  </div>
  <div class="labels">
    <div class="label">Tidewater Imports<span>+more</span></div>
    <div class="label">Harbor Weave<span>+more</span></div>
    <div class="label">Crimson Sala Co<span>+more</span></div>
  </div>
</main>

<aside class="abs related">
  <div class="related-inner">
    <div class="related-head">YOU MAY ALSO LIKE</div>
    <div class="card"><div class="card-art" role="img" aria-label="Modern rug with black, red and grey waves" style="background:linear-gradient(180deg,#333,#b23 50%,#999)"></div><div class="card-name">Harbor Weave</div><div class="card-price">$29.59 - $422.40</div></div>
    <div class="card"><div class="card-art" role="img" aria-label="Tan and brown swirl rug" style="background:linear-gradient(135deg,#c79a5a,#4a2a14)"></div><div class="card-name">Tidewater Imports</div><div class="card-price">$49.00 - $560.00</div></div>
    <div class="card"><div class="card-art" role="img" aria-label="Grey concentric circle rug" style="background:radial-gradient(circle,#eee,#555 50%,#222)"></div><div class="card-name">Solmara</div><div class="card-price">$35.00 - $303.00</div></div>
    <div class="card"><div class="card-art" role="img" aria-label="Brown and cream block pattern rug" style="background:linear-gradient(90deg,#7a6a5e,#3a2a22 50%,#c9bfae)"></div><div class="card-name">Corvell</div><div class="card-price">$49.00 - $629.00</div></div>
    <div class="card"><div class="card-art" role="img" aria-label="Gold and cream ornamental rug" style="background:linear-gradient(135deg,#d2b46e,#a88340)"></div><div class="card-name">Corvell</div><div class="card-price">$49.00 - $629.00</div></div>
  </div>
</aside>

<footer>
  <div class="abs footer-rule"></div>
  <div class="abs footer-rule2"></div>
  <div class="abs fcol" style="left:20px">
    <h3>Customer Service</h3>
    Shipping<br>Return Policy<br>Privacy Policy<br>Ordering &amp; Delivery Checklist<br>Terms of Use<br>Terms of Sale<br>Contact Us<br>Environmental Policy
  </div>
  <div class="abs fcol" style="left:257px">
    <h3>Customer Service</h3>
    Product Articles<br>Learning Center<br>Help<br>Refer A Friend<br>LoomNest Blog<br>Room Scene Viewer<br>Site Map<br>FAQ<br>Customer Testimonials<br>Photo Gallery
  </div>
  <div class="abs fcol" style="left:494px">
    <h3>Corporate Info</h3>
    About LoomNest.com<br>Careers<br>Affiliates
  </div>
  <div class="abs badges">
    <span class="badge" style="width:44px;background:#2d5aa6"></span>
    <span class="badge" style="width:40px;background:#e0e0e0"></span>
    <span class="badge" style="width:42px;background:#f0e6d8"></span>
    <span class="badge" style="width:42px;background:#3f8ccb"></span>
    <span class="badge" style="width:42px;background:#e6eef6"></span>
    <span class="badge" style="width:44px;background:#eee"></span>
    <span class="badge" style="width:46px;height:42px;border-radius:50%;background:#e8c94a"></span>
    <span class="badge" style="width:44px;height:42px;border-radius:50%;background:#e8c94a"></span>
    <span class="badge" style="width:56px;background:#ddd"></span>
    <span class="badge" style="width:58px;background:#2c5aa0"></span>
    <span class="badge" style="width:72px;background:#d5d5d5"></span>
  </div>
</footer>

</body>
</html>
```